Start out business card needed

We have uploaded a flyer we like the design of for inspiration for the business card.

Target Market(s)

Fitness lovers

Industry/Entity Type

Health And Wellness

Contact Information for Business Card

Business Development Manager
Mick de la porte
Phone number to be advised
Mick@lift-yard.com.au
www.lift-yard.com.au

Font styles to use
Sans Serif

Colors
fbee3e
1b1b1b
f5f5f5

Requirements
Must have
• Front : Logo (large should take up most of the space)
• Back : small logo, business details

```html
<!DOCTYPE html>
<html lang="en">
<head>
<meta charset="utf-8">
<title>Lift Yard – Business Card</title>
<link href="https://fonts.googleapis.com/css2?family=Oswald:wght@500&family=Open+Sans:wght@300;400;700&display=swap" rel="stylesheet">
<style>
  :root{
    --bg:#65718a;
    --paper:#f5f5f5;
    --ink:#1b1b1b;
    --gold:#eeb115;
    --gold-light:#fbc91a;
    --gold-deep:#dca010;
    --band-dark:#1f1f1f;
    --band-mid:#5a5a5a;
    --white:#ffffff;
  }
  *{margin:0;padding:0;box-sizing:border-box}
  html,body{width:1200px;height:810px;overflow:hidden;background:var(--bg)}
  .canvas{position:relative;width:1200px;height:810px;background:radial-gradient(ellipse at 50% 20%,#8690a4 0%,var(--bg) 70%)}
  .card{position:absolute;top:250px;width:540px;height:310px;background:var(--paper);overflow:hidden;box-shadow:0 18px 30px rgba(20,25,40,.35)}
  .card--back{left:40px}
  .card--front{left:620px}
  .card svg.shapes{position:absolute;inset:0}
  .photo-band{position:absolute;left:0;top:0;width:540px;height:96px;background:linear-gradient(100deg,var(--band-dark) 0%,var(--band-mid) 45%,#2a2a2a 75%,#6b6b6b 100%)}
  .holder{position:absolute;left:24px;top:22px;color:var(--white)}
  .holder__name{font-family:'Open Sans',sans-serif;font-weight:700;font-size:24px;letter-spacing:-.2px;line-height:1.1}
  .holder__title{font-family:'Open Sans',sans-serif;font-weight:300;font-size:13px;letter-spacing:.6px;margin-top:4px}
  .contacts{position:absolute;left:24px;top:114px;list-style:none;color:var(--white);font-family:'Open Sans',sans-serif;font-size:11.5px;line-height:1.45}
  .contacts li{display:flex;gap:8px;margin-bottom:6px}
  .contacts svg{flex:none;margin-top:2px}
  .logo{position:absolute;display:flex;align-items:center;gap:12px;font-family:'Oswald',sans-serif;font-weight:500;color:var(--ink);letter-spacing:2px;white-space:nowrap}
  .logo__mark{background:var(--ink)}
  .card--back .logo{right:28px;bottom:38px;font-size:34px}
  .card--back .logo__mark{width:14px;height:14px}
  .card--front .logo{left:44px;top:118px;font-size:58px}
  .card--front .logo__mark{width:22px;height:22px}
</style>
</head>
<body>
<main class="canvas">

  <section class="card card--back" aria-label="Card back">
    <svg class="shapes" width="540" height="310" viewBox="0 0 540 310">
      <path d="M0 96 H330 C318 200 210 262 0 268 Z" fill="var(--gold-light)"/>
      <path d="M0 96 H330 C318 190 205 248 0 252 Z" fill="var(--gold)"/>
    </svg>
    <div class="photo-band" role="img" aria-label="Black-and-white photo of an athlete with wrapped hands"></div>
    <div class="holder">
      <p class="holder__name">Mick de la porte</p>
      <p class="holder__title">Business Development Manager</p>
    </div>
    <ul class="contacts">
      <li>
        <svg width="11" height="11" viewBox="0 0 12 12"><path d="M6 1 L11 6 H9.5 V11 H2.5 V6 H1 Z" fill="#fff"/></svg>
        <span>1450 Harbor Mill Rd, Ste 120,<br>Seaside Point, CA 90001</span>
      </li>
      <li>
        <svg width="11" height="11" viewBox="0 0 12 12"><path d="M3 1 L5 3.5 L4 5 C4.8 6.6 5.6 7.4 7 8 L8.5 7 L11 9 L9.5 11 C5 10.5 1.5 7 1 2.5 Z" fill="#fff"/></svg>
        <span>555 010 2846</span>
      </li>
      <li>
        <svg width="11" height="11" viewBox="0 0 12 12"><rect x="1" y="2.5" width="10" height="7" fill="#fff"/><path d="M1 2.5 L6 6.5 L11 2.5" stroke="var(--gold)" stroke-width="1" fill="none"/></svg>
        <span>Mick@lift-yard.com.au<br>www.lift-yard.com.au</span>
      </li>
    </ul>
    <div class="logo"><span class="logo__mark"></span>LIFT YARD</div>
  </section>

  <section class="card card--front" aria-label="Card front">
    <svg class="shapes" width="540" height="310" viewBox="0 0 540 310">
      <path d="M392 0 C372 110 380 230 430 310 H540 V0 Z" fill="var(--gold-light)"/>
      <path d="M408 0 C388 110 396 230 446 310 H540 V0 Z" fill="var(--gold)"/>
      <path d="M470 0 C450 120 460 230 500 310 H540 V0 Z" fill="var(--gold-deep)" opacity=".35"/>
    </svg>
    <div class="logo"><span class="logo__mark"></span>LIFT YARD</div>
  </section>

</main>
</body>
</html>
```